Velsori Biotechnology needs a professional powerpoint design

We would like to re-design our powerpoint template(as attachment 1), it should be based on our current logo (as attachment 2). We hope the new powerpoint template could be more professional and like a biotechnology company with advanced technology.
Velsori Biotechnology is a contract development and manufacturing organization to provide high quality services to our clients in development, lead-in advanced technology and cGMP manufacturing of biopharmaceuticals from clinical to commercial manufacturing. We offers the advanced technology and services to become the best partner for clients from clinical to commercial manufacturing.
Reason: We would like to extend the deadline for this project so that designers can have more time to prepare, thanks.
Target Market(s)
Velsori Biotechnology is a contract development and manufacturing organization to provide high quality services to our clients in development, lead-in advanced technology and cGMP manufacturing of biopharmaceuticals from clinical to commercial manufacturing.
Velsori primary focus on development and manufacturing of glycoprotein pharmaceuticals against breast cancer, supplies KEP Taiwan with KEP-437 & KEP-438 for global clinical trials and commercialization in the future. Velsori offers the advanced technology and services to become the best partner for clients from clinical to commercial manufacturing.
Industry/Entity Type
Biotechnology
Requirements
Must have
- The new powerpoint design should based on our current logo.
Should not have
- The similar design with current powerpoint style. Please don't refer the design style of our current website http://www.velsori-example.com.tw/ as well, we will re-design it soon.

```html
<!DOCTYPE html>
<html lang="en">
<head>
<meta charset="utf-8">
<title>Velsori Biotechnology – Presentation Template</title>
<link href="https://fonts.googleapis.com/css2?family=Arimo:ital,wght@0,400;0,700;1,400;1,700&display=swap" rel="stylesheet">
<style>
:root{
  --blue:#2b4aa8;
  --blue-band:#5b8bd6;
  --blue-soft:#c9d9f1;
  --green:#8ab848;
  --green-dark:#2f4a1e;
  --green-mid:#7fa34f;
  --green-pale:#eaf3d6;
  --green-wash:#dde9cf;
  --red:#d9372b;
  --ink:#333;
  --grey:#d9d9d9;
}
*{box-sizing:border-box;margin:0;padding:0}
html,body{width:1200px;height:1200px;overflow:hidden;background:#fff;font-family:"Arimo",Arial,sans-serif;color:var(--ink)}
.sheet{position:relative;width:1200px;height:1200px}
.slide{position:absolute;width:254px;height:142px;background:#fff;overflow:hidden;box-shadow:1px 2px 3px rgba(0,0,0,.3)}
.slide.wash{background:linear-gradient(135deg,#eef4e6,#d6e6c8 60%,#eef4e6)}
.bar-top{position:absolute;left:0;top:0;width:100%;height:4px;background:var(--blue-band)}
.bar-bottom{position:absolute;left:0;bottom:0;width:100%;height:4px;background:var(--green)}
.title{position:absolute;left:15px;top:12px;font-size:7.6px;font-style:italic;color:var(--blue);letter-spacing:.1px;white-space:nowrap}
.sub{position:absolute;left:15px;top:22px;font-size:3.8px;font-weight:700;font-style:italic;color:#222}
.logo{position:absolute;right:9px;top:10px;display:flex;align-items:center;gap:2px;font-size:5.4px;font-weight:700;color:#222;letter-spacing:.3px}
.logo i{width:4px;height:4px;border-radius:50%;background:var(--green);display:block}
.logo.bottom{top:auto;bottom:9px}
.txt{position:absolute;font-size:2.6px;line-height:3.3px;color:#444}
.txt b{font-size:3.4px;color:#222}
.photo{position:absolute;display:block}
.ph-blue{background:linear-gradient(135deg,#1c2f4f,#5b86b8 60%,#bcd0e6)}
.ph-green{background:linear-gradient(135deg,#2d4a22,#8ab848 60%,#d5e8b8)}
.ph-lab{background:linear-gradient(135deg,#e4ecf3,#9fb8cf 55%,#6f8a5a)}
.ph-dark{background:linear-gradient(160deg,#101418,#3b4a3e 55%,#9fb86b)}
.ph-earth{background:radial-gradient(circle at 40% 40%,#6ab04c,#1f5c8f 60%,#0f2740)}
.bullets{list-style:none}
.bullets li{position:relative;padding-left:4px;margin-bottom:2.6px}
.bullets li::before{content:"";position:absolute;left:0;top:1px;width:1.4px;height:1.4px;border-radius:50%;background:#555}
svg{position:absolute;display:block}
.cap{font-size:3.4px;font-weight:700;color:#222;text-align:center}
table{border-collapse:collapse}
.tbl{position:absolute;font-size:2.4px;color:#333}
.tbl td,.tbl th{padding:0 1.5px;height:5.4px;border-bottom:.3px solid #bbb;text-align:right;font-weight:400}
.tbl td:first-child,.tbl th:first-child{text-align:left}
.tbl th{background:var(--green);color:#fff}
.tbl tr.total td{border-top:.6px solid #555;font-weight:700}
</style>
</head>
<body>
<div class="sheet">

<!-- Row 1 -->
<section class="slide" style="left:43px;top:36px">
  <svg width="254" height="142" viewBox="0 0 254 142">
    <defs><linearGradient id="coverA" x1="0" y1="0" x2="1" y2="1"><stop offset="0" stop-color="#2c3138"/><stop offset=".55" stop-color="#7f8a86"/><stop offset="1" stop-color="#cfd8c2"/></linearGradient></defs>
    <path d="M0 0H160Q140 80 120 142H0Z" fill="url(#coverA)" role="img" aria-label="Photo of a gloved hand holding a green seedling in a lab"/>
    <path d="M160 0Q140 80 120 142" fill="none" stroke="var(--blue)" stroke-width="2"/>
  </svg>
  <div style="position:absolute;right:9px;top:8px;text-align:right;font-size:11.5px;line-height:17px;font-style:italic;color:#222">LOREM<br>IPSUM<br>DOLOR</div>
  <div class="txt" style="right:9px;top:61px;text-align:right;width:50px">Lorem ipsum dolor sit amet, consetetur sadipscing</div>
  <div class="logo" style="top:auto;bottom:12px;right:20px;font-size:12px;gap:4px"><i style="width:8px;height:8px"></i>VELSORI</div>
</section>

<section class="slide" style="left:328px;top:36px">
  <svg width="254" height="142" viewBox="0 0 254 142">
    <path d="M0 0H254V14Q110 4 0 52Z" fill="var(--blue-soft)"/>
    <path d="M254 14Q110 4 0 52" fill="none" stroke="var(--blue)" stroke-width="2"/>
  </svg>
  <div class="logo" style="top:62px;right:12px;font-size:14px;gap:4px"><i style="width:9px;height:9px"></i>VELSORI</div>
  <div style="position:absolute;left:0;top:100px;width:100%;height:34px;background:var(--green)"></div>
  <div style="position:absolute;left:15px;top:107px;font-size:8.6px;font-style:italic;color:#fff">LOREM IPSUM DOLOR</div>
  <div style="position:absolute;left:15px;top:119px;font-size:3.2px;color:#fff">Lorem ipsum dolor sit amet, consetetur sadipscing</div>
</section>

<section class="slide" style="left:612px;top:36px">
  <div class="photo ph-dark" style="left:0;top:0;width:46px;height:142px" role="img" aria-label="Photo of laboratory equipment with glowing light"></div>
  <div class="photo ph-lab" style="left:48px;top:0;width:48px;height:142px" role="img" aria-label="Photo of a gloved hand holding a seedling"></div>
  <div class="title" style="left:107px;top:15px">LOREM IPSUM</div>
  <div class="txt" style="left:107px;top:26px;font-size:3.2px">Dolor sit amet</div>
  <ul class="txt bullets" style="left:110px;top:42px;width:118px">
    <li>Lorem ipsum dolor sit amet, consetetur sadipscing elitr, sed diam nonumy eirmod tempor invidunt ut labore et dolore magna aliquyam erat, sed diam voluptua. At vero eos et accusam</li>
    <li>Lorem ipsum dolor sit amet, consetetur sadipscing elitr, sed diam nonumy eirmod tempor invidunt ut labore et dolore magna aliquyam erat, sed diam voluptua. At vero eos et accusam</li>
    <li>Lorem ipsum dolor sit amet, consetetur sadipscing elitr, sed diam nonumy eirmod tempor invidunt ut labore et dolore magna aliquyam erat, sed diam voluptua. At vero eos et accusam</li>
  </ul>
  <div class="logo bottom"><i></i>VELSORI</div>
</section>

<section class="slide" style="left:896px;top:36px">
  <div class="bar-top"></div>
  <div class="title">LOREM IPSUM DOLOR SIT AMET</div>
  <div class="sub">Consetetur sadipscing elitr</div>
  <div class="logo"><i></i>VELSORI</div>
  <div class="photo ph-lab" style="left:0;top:43px;width:63px;height:42px" role="img" aria-label="Photo of a scientist beside a globe"></div>
  <div class="photo ph-blue" style="left:63px;top:43px;width:64px;height:42px" role="img" aria-label="Photo of plants growing in a lab"></div>
  <div class="photo ph-green" style="left:127px;top:43px;width:64px;height:42px" role="img" aria-label="Photo of test tubes with green samples"></div>
  <div class="photo ph-earth" style="left:191px;top:43px;width:63px;height:42px" role="img" aria-label="Photo of a seedling on a globe"></div>
  <div class="txt" style="left:15px;top:91px;width:105px">Lorem ipsum dolor sit amet, consetetur sadipscing elitr, sed diam nonumy eirmod tempor invidunt ut labore et dolore magna aliquyam erat, sed diam voluptua. At vero eos et accusam. Lorem ipsum dolor sit amet, consetetur sadipscing elitr, sed diam nonumy eirmod tempor invidunt ut labore et dolore magna aliquyam erat.</div>
  <div class="txt" style="left:130px;top:91px;width:105px">Lorem ipsum dolor sit amet, consetetur sadipscing elitr, sed diam nonumy eirmod tempor invidunt ut labore et dolore magna aliquyam erat, sed diam voluptua. At vero eos et accusam. Lorem ipsum dolor sit amet, consetetur sadipscing elitr, sed diam nonumy eirmod tempor invidunt ut labore et dolore magna aliquyam erat.</div>
  <div class="bar-bottom"></div>
</section>

<!-- Row 2 -->
<section class="slide" style="left:43px;top:218px">
  <div class="bar-top"></div>
  <div class="title">LOREM IPSUM DOLOR SIT AMET</div>
  <div class="sub">Consetetur sadipscing elitr</div>
  <div class="logo"><i></i>VELSORI</div>
  <div class="photo ph-lab" style="left:21px;top:36px;width:46px;height:46px;border-radius:50%" role="img" aria-label="Photo of a scientist beside a globe"></div>
  <div class="photo ph-earth" style="left:77px;top:36px;width:46px;height:46px;border-radius:50%" role="img" aria-label="Photo of a seedling on a globe"></div>
  <div class="photo ph-dark" style="left:133px;top:36px;width:46px;height:46px;border-radius:50%" role="img" aria-label="Photo of a globe with plants"></div>
  <div class="photo ph-green" style="left:189px;top:36px;width:46px;height:46px;border-radius:50%;background:linear-gradient(135deg,#f2efe6,#cfe0b3 60%,#8ab848)" role="img" aria-label="Photo of a hand holding a test tube"></div>
  <div class="cap" style="position:absolute;left:19px;top:87px;width:50px">Lorem ipsum</div>
  <div class="cap" style="position:absolute;left:75px;top:87px;width:50px">Lorem ipsum</div>
  <div class="cap" style="position:absolute;left:131px;top:87px;width:50px">Lorem ipsum</div>
  <div class="cap" style="position:absolute;left:187px;top:87px;width:50px">Lorem ipsum</div>
  <div class="txt" style="left:19px;top:93px;width:50px;text-align:center">Lorem ipsum dolor sit amet, consetetur sadipscing elitr, sed diam nonumy eirmod tempor invidunt ut labore et dolore magna aliquyam erat, sed diam voluptua.</div>
  <div class="txt" style="left:75px;top:93px;width:50px;text-align:center">Lorem ipsum dolor sit amet, consetetur sadipscing elitr, sed diam nonumy eirmod tempor invidunt ut labore et dolore magna aliquyam erat, sed diam voluptua.</div>
  <div class="txt" style="left:131px;top:93px;width:50px;text-align:center">Lorem ipsum dolor sit amet, consetetur sadipscing elitr, sed diam nonumy eirmod tempor invidunt ut labore et dolore magna aliquyam erat, sed diam voluptua.</div>
  <div class="txt" style="left:187px;top:93px;width:50px;text-align:center">Lorem ipsum dolor sit amet, consetetur sadipscing elitr, sed diam nonumy eirmod tempor invidunt ut labore et dolore magna aliquyam erat, sed diam voluptua.</div>
  <div class="bar-bottom"></div>
</section>

<section class="slide wash" style="left:328px;top:218px" role="img" aria-label="Slide with faint laboratory photo background">
  <div class="bar-top"></div>
  <div class="title">LOREM IPSUM DOLOR SIT AMET</div>
  <div class="logo"><i></i>VELSORI</div>
  <div class="photo ph-blue" style="left:18px;top:39px;width:68px;height:38px" role="img" aria-label="Photo of a hand in a glowing lab scene"></div>
  <div class="photo ph-blue" style="left:93px;top:39px;width:68px;height:38px;background:linear-gradient(135deg,#0d1d3a,#2f5fa0 55%,#9cc0e8)" role="img" aria-label="Image of a DNA helix"></div>
  <div class="photo ph-lab" style="left:168px;top:39px;width:68px;height:38px" role="img" aria-label="Photo of a pipette over sample tubes"></div>
  <div class="txt" style="left:20px;top:82px;width:64px;text-align:center">Lorem ipsum dolor sit amet, consetetur sadipscing elitr, sed diam nonumy eirmod tempor invidunt ut labore et dolore magna aliquyam erat, sed diam</div>
  <div class="txt" style="left:95px;top:82px;width:64px;text-align:center">Lorem ipsum dolor sit amet, consetetur sadipscing elitr, sed diam nonumy eirmod tempor invidunt ut labore et dolore magna aliquyam erat, sed diam</div>
  <div class="txt" style="left:170px;top:82px;width:64px;text-align:center">Lorem ipsum dolor sit amet, consetetur sadipscing elitr, sed diam nonumy eirmod tempor invidunt ut labore et dolore magna aliquyam erat, sed diam</div>
  <div class="bar-bottom"></div>
</section>

<section class="slide wash" style="left:612px;top:218px" role="img" aria-label="Slide with faint laboratory photo background">
  <div class="bar-top"></div>
  <div class="title">LOREM IPSUM DOLOR SIT AMET</div>
  <div class="logo"><i></i>VELSORI</div>
  <div class="photo ph-blue" style="left:13px;top:34px;width:84px;height:32px" role="img" aria-label="Photo of a hand in a glowing lab scene"></div>
  <div class="photo ph-blue" style="left:13px;top:67px;width:84px;height:32px;background:linear-gradient(135deg,#0d1d3a,#2f5fa0 55%,#9cc0e8)" role="img" aria-label="Image of a DNA helix"></div>
  <div class="photo ph-lab" style="left:13px;top:100px;width:84px;height:33px" role="img" aria-label="Photo of a scientist working with samples"></div>
  <div class="txt" style="left:101px;top:40px;width:125px">Lorem ipsum dolor sit amet, consetetur sadipscing elitr, sed diam nonumy eirmod tempor invidunt ut labore et dolore magna aliquyam erat, sed diam voluptua. At vero eos et accusam et justo duo dolores et ea rebum.</div>
  <div class="txt" style="left:101px;top:74px;width:125px">Lorem ipsum dolor sit amet, consetetur sadipscing elitr, sed diam nonumy eirmod tempor invidunt ut labore et dolore magna aliquyam erat, sed diam voluptua. At vero eos et accusam et justo duo dolores et ea rebum.</div>
  <div class="txt" style="left:101px;top:108px;width:125px">Lorem ipsum dolor sit amet, consetetur sadipscing elitr, sed diam nonumy eirmod tempor invidunt ut labore et dolore magna aliquyam erat, sed diam voluptua. At vero eos et accusam et justo duo dolores et ea rebum.</div>
  <div class="bar-bottom"></div>
</section>

<section class="slide" style="left:896px;top:218px">
  <div class="bar-top"></div>
  <svg width="254" height="142" viewBox="0 0 254 142"><path d="M254 4V138H196Q240 90 248 4Z" fill="var(--green-pale)"/><path d="M248 4Q240 90 196 138" fill="none" stroke="var(--green)" stroke-width="1.6"/></svg>
  <div class="title">LOREM IPSUM DOLOR SIT AMET</div>
  <div class="txt" style="left:15px;top:40px;width:200px"><b>Lorem ipsum dolor sit amet,</b> consetetur sadipscing elitr, sed diam nonumy eirmod tempor invidunt ut labore et dolore magna aliquyam erat, sed diam voluptua. At vero eos et accusam et justo duo dolores et ea rebum. Stet clita kasd gubergren, no sea takimata sanctus est.</div>
  <div class="txt" style="left:15px;top:62px;width:200px"><b>Lorem ipsum dolor sit amet,</b> consetetur sadipscing elitr, sed diam nonumy eirmod tempor invidunt ut labore et dolore magna aliquyam erat, sed diam voluptua. At vero eos et accusam et justo duo dolores et ea rebum. Stet clita kasd gubergren, no sea takimata sanctus est.</div>
  <div class="txt" style="left:15px;top:84px;width:200px"><b>Lorem ipsum dolor sit amet,</b> consetetur sadipscing elitr, sed diam nonumy eirmod tempor invidunt ut labore et dolore magna aliquyam erat, sed diam voluptua. At vero eos et accusam et justo duo dolores et ea rebum. Stet clita kasd gubergren, no sea takimata sanctus est.</div>
  <div class="txt" style="left:15px;top:106px;width:200px"><b>Lorem ipsum dolor sit amet,</b> consetetur sadipscing elitr, sed diam nonumy eirmod tempor invidunt ut labore et dolore magna aliquyam erat, sed diam voluptua. At vero eos et accusam et justo duo dolores et ea rebum. Stet clita kasd gubergren, no sea takimata sanctus est.</div>
  <div class="logo bottom"><i></i>VELSORI</div>
  <div class="bar-bottom"></div>
</section>

<!-- Row 3 -->
<section class="slide" style="left:43px;top:400px">
  <div class="bar-top"></div>
  <svg width="254" height="142" viewBox="0 0 254 142"><path d="M254 4V138H210Q236 70 254 4Z" fill="var(--green-pale)"/><path d="M254 4Q236 70 210 138" fill="none" stroke="var(--green)" stroke-width="1.6"/></svg>
  <div class="title">LOREM IPSUM DOLOR SIT AMET</div>
  <svg width="230" height="110" viewBox="0 0 230 110" style="left:14px;top:33px">
    <g font-size="3" fill="var(--green)" font-family="Arimo,Arial,sans-serif" font-weight="700">
      <text transform="translate(5 21) rotate(-90)">TITLE</text>
      <text transform="translate(5 46) rotate(-90)">TITLE</text>
      <text transform="translate(5 71) rotate(-90)">TITLE</text>
      <text transform="translate(5 96) rotate(-90)">TITLE</text>
    </g>
    <g fill="none" stroke="var(--green)" stroke-width=".6">
      <rect x="60" y="3" width="168" height="20"/><rect x="60" y="28" width="168" height="20"/>
      <rect x="60" y="53" width="168" height="20"/><rect x="60" y="78" width="168" height="20"/>
    </g>
    <g fill="var(--green)">
      <path d="M10 3H64L70 13L64 23H10Z"/><path d="M10 28H64L70 38L64 48H10Z"/>
      <path d="M10 53H64L70 63L64 73H10Z"/><path d="M10 78H64L70 88L64 98H10Z"/>
    </g>
  </svg>
  <div class="txt" style="left:30px;top:40px;width:45px;color:#fff;text-align:center">Lorem ipsum dolor sit amet, consetetur sadipscing elitr</div>
  <div class="txt" style="left:30px;top:65px;width:45px;color:#fff;text-align:center">Lorem ipsum dolor sit amet, consetetur sadipscing elitr</div>
  <div class="txt" style="left:30px;top:90px;width:45px;color:#fff;text-align:center">Lorem ipsum dolor sit amet, consetetur sadipscing elitr</div>
  <div class="txt" style="left:30px;top:115px;width:45px;color:#fff;text-align:center">Lorem ipsum dolor sit amet, consetetur sadipscing elitr</div>
  <div class="txt" style="left:90px;top:39px;width:148px">Lorem ipsum dolor sit amet, consetetur sadipscing elitr, sed diam nonumy eirmod tempor invidunt ut labore et dolore magna aliquyam erat, sed diam voluptua. At vero eos et accusam et justo duo dolores et ea rebum.</div>
  <div class="txt" style="left:90px;top:64px;width:148px">Lorem ipsum dolor sit amet, consetetur sadipscing elitr, sed diam nonumy eirmod tempor invidunt ut labore et dolore magna aliquyam erat, sed diam voluptua. At vero eos et accusam et justo duo dolores et ea rebum.</div>
  <div class="txt" style="left:90px;top:89px;width:148px">Lorem ipsum dolor sit amet, consetetur sadipscing elitr, sed diam nonumy eirmod tempor invidunt ut labore et dolore magna aliquyam erat, sed diam voluptua. At vero eos et accusam et justo duo dolores et ea rebum.</div>
  <div class="txt" style="left:90px;top:114px;width:148px">Lorem ipsum dolor sit amet, consetetur sadipscing elitr, sed diam nonumy eirmod tempor invidunt ut labore et dolore magna aliquyam erat, sed diam voluptua. At vero eos et accusam et justo duo dolores et ea rebum.</div>
  <div class="logo bottom"><i></i>VELSORI</div>
  <div class="bar-bottom"></div>
</section>

<section class="slide wash" style="left:328px;top:400px" role="img" aria-label="Slide with faint laboratory photo background">
  <div class="bar-top"></div>
  <div class="title">LOREM IPSUM DOLOR SIT AMET</div>
  <div class="sub">Consetetur sadipscing elitr</div>
  <div class="logo"><i></i>VELSORI</div>
  <svg width="240" height="82" viewBox="0 0 240 82" style="left:24px;top:44px">
    <path d="M0 0H70L88 41L70 82H0L18 41Z" fill="var(--green-dark)"/>
    <path d="M72 0H140L158 41L140 82H72L90 41Z" fill="var(--green-mid)" opacity=".85"/>
    <path d="M142 0H210L228 41L210 82H142L160 41Z" fill="#b7cf98" opacity=".8"/>
    <g font-family="Arimo,Arial,sans-serif" font-size="5.6" font-weight="700" fill="#fff">
      <text x="24" y="13">TITLE</text><text x="96" y="13">TITLE</text><text x="166" y="13">TITLE</text>
    </g>
  </svg>
  <div class="txt" style="left:46px;top:62px;width:44px;color:#fff;font-size:3px;line-height:4px">Lorem ipsum dolor sit amet, consetetur sadipscing elitr, sed diam nonumy eirmo d. Tempor invidunt u t labore et dolore m agna aliquyam erat, sed diam voluptua</div>
  <div class="txt" style="left:118px;top:62px;width:44px;color:#fff;font-size:3px;line-height:4px">Lorem ipsum dolor sit amet, consetetur sadipscing elitr, sed diam nonumy eirmo d. Tempor invidunt u t labore et dolore m agna aliquyam erat, sed diam voluptua</div>
  <div class="txt" style="left:188px;top:62px;width:44px;color:#fff;font-size:3px;line-height:4px">Lorem ipsum dolor sit amet, consetetur sadipscing elitr, sed diam nonumy eirmo d. Tempor invidunt u t labore et dolore m agna aliquyam erat, sed diam voluptua</div>
  <div class="bar-bottom"></div>
</section>

<section class="slide" style="left:612px;top:400px">
  <div class="bar-top"></div>
  <svg width="254" height="142" viewBox="0 0 254 142"><path d="M254 4V138H210Q236 70 254 4Z" fill="var(--green-pale)"/><path d="M254 4Q236 70 210 138" fill="none" stroke="var(--green)" stroke-width="1.6"/></svg>
  <div class="title">LOREM IPSUM DOLOR SIT AMET</div>
  <div class="sub">Consetetur sadipscing elitr</div>
  <ul class="txt bullets" style="left:18px;top:42px;width:80px">
    <li>Lorem ipsum dolor sit amet, consetetur sadipscing elitr, sed diam nonumy eirmod tempor invidunt ut labore et dolore magna aliquyam erat, sed diam voluptua. At vero eos et accusam</li>
    <li>Lorem ipsum dolor sit amet, consetetur sadipscing elitr, sed diam nonumy eirmod tempor invidunt ut labore et dolore magna aliquyam erat, sed diam voluptua. At vero eos et accusam</li>
    <li>Lorem ipsum dolor sit amet, consetetur sadipscing elitr, sed diam nonumy eirmod tempor invidunt ut labore et dolore magna aliquyam erat, sed diam voluptua. At vero eos et accusam</li>
  </ul>
  <svg width="80" height="90" viewBox="0 0 80 90" style="left:120px;top:44px">
    <line x1="2" y1="74" x2="78" y2="74" stroke="#bbb" stroke-width=".4"/>
    <rect x="6" y="10" width="2.4" height="64" fill="var(--green)"/><rect x="9" y="42" width="2.4" height="32" fill="var(--red)"/><rect x="12" y="46" width="2.4" height="28" fill="var(--blue)"/>
    <rect x="30" y="40" width="2.4" height="34" fill="var(--green)"/><rect x="33" y="2" width="2.4" height="72" fill="var(--red)"/><rect x="36" y="36" width="2.4" height="38" fill="var(--blue)"/>
    <rect x="54" y="18" width="2.4" height="56" fill="var(--green)"/><rect x="57" y="44" width="2.4" height="30" fill="var(--red)"/><rect x="60" y="26" width="2.4" height="48" fill="var(--blue)"/>
    <g font-size="2" fill="#555" font-family="Arimo,Arial,sans-serif"><text x="7" y="79">Text</text><text x="31" y="79">Text</text><text x="55" y="79">Text</text>
    <rect x="18" y="85" width="2" height="1.6" fill="var(--green)"/><text x="21" y="86.5">Text</text><rect x="32" y="85" width="2" height="1.6" fill="var(--red)"/><text x="35" y="86.5">Text2</text><rect x="48" y="85" width="2" height="1.6" fill="var(--blue)"/><text x="51" y="86.5">Text3</text></g>
  </svg>
  <div class="logo bottom"><i></i>VELSORI</div>
  <div class="bar-bottom"></div>
</section>

<section class="slide" style="left:896px;top:400px">
  <div class="bar-top"></div>
  <svg width="254" height="142" viewBox="0 0 254 142"><path d="M254 4V138H210Q236 70 254 4Z" fill="var(--green-pale)"/><path d="M254 4Q236 70 210 138" fill="none" stroke="var(--green)" stroke-width="1.6"/></svg>
  <div class="title">LOREM IPSUM DOLOR SIT AMET</div>
  <svg width="254" height="142" viewBox="0 0 254 142">
    <g font-family="Arimo,Arial,sans-serif" text-anchor="middle">
      <text x="62" y="39" font-size="3.4" fill="#333">LOREM IPSUM</text>
      <text x="153" y="39" font-size="3.4" fill="#333">LOREM IPSUM</text>
      <circle cx="62" cy="76" r="28" fill="none" stroke="#e3e3e3" stroke-width="9"/>
      <circle cx="62" cy="76" r="28" fill="none" stroke="var(--green)" stroke-width="9" stroke-dasharray="161.8 176" transform="rotate(-90 62 76)"/>
      <circle cx="153" cy="76" r="28" fill="none" stroke="#e3e3e3" stroke-width="9"/>
      <circle cx="153" cy="76" r="28" fill="none" stroke="var(--green)" stroke-width="9" stroke-dasharray="146 176" transform="rotate(-90 153 76)"/>
      <text x="62" y="79.5" font-size="9.5" fill="#333">+92%</text>
      <text x="153" y="79.5" font-size="9.5" fill="#333">+83%</text>
    </g>
  </svg>
  <div class="txt" style="left:30px;top:114px;width:150px;text-align:center">Lorem ipsum dolor sit amet, consetetur sadipscing elitr, sed diam nonumy eirmod tempor invidunt ut. Lorem ipsum dolor sit amet, consetetur sadipscing elitr, sed diam nonumy eirmod tempor invidunt ut.</div>
  <div class="logo bottom"><i></i>VELSORI</div>
  <div class="bar-bottom"></div>
</section>

<!-- Row 4 -->
<section class="slide" style="left:43px;top:582px">
  <div class="bar-top"></div>
  <div class="title">LOREM IPSUM DOLOR SIT AMET</div>
  <div class="sub">Consetetur sadipscing elitr</div>
  <div class="logo"><i></i>VELSORI</div>
  <svg width="240" height="70" viewBox="0 0 240 70" style="left:14px;top:39px">
    <g font-family="Arimo,Arial,sans-serif" font-size="2.6" fill="#555">
      <text x="2" y="3" font-size="3.4" fill="#222">Title <tspan font-size="2">(Text)</tspan></text>
      <text x="122" y="3" font-size="3.4" fill="#222">Title <tspan font-size="2">(Text)</tspan></text>
      <text x="3" y="9">70</text><text x="3" y="16">60</text><text x="3" y="23">50</text><text x="3" y="30">40</text><text x="3" y="37">30</text><text x="3" y="44">20</text><text x="3" y="51">10</text><text x="5" y="58">0</text>
      <text x="123" y="9">70</text><text x="123" y="16">60</text><text x="123" y="23">50</text><text x="123" y="30">40</text><text x="123" y="37">30</text><text x="123" y="44">20</text><text x="123" y="51">10</text><text x="125" y="58">0</text>
      <text x="20" y="64">Text  Text  Text  Text  Text  Text  Text  Text</text>
      <text x="140" y="64">Text  Text  Text  Text  Text  Text  Text  Text</text>
    </g>
    <g stroke="#e5e5e5" stroke-width=".3"><path d="M10 8H110M10 15H110M10 22H110M10 29H110M10 36H110M10 43H110M10 50H110M10 57H110"/><path d="M130 8H230M130 15H230M130 22H230M130 29H230M130 36H230M130 43H230M130 50H230M130 57H230"/></g>
    <polyline points="14,50 28,40 42,14 56,12 70,20 84,20 98,18" fill="none" stroke="var(--blue)" stroke-width=".8"/>
    <polyline points="14,46 28,34 42,12 56,22 70,28 84,18 98,20" fill="none" stroke="var(--green)" stroke-width=".8"/>
    <polyline points="134,20 148,14 162,20 176,10 190,22 204,12 218,20" fill="none" stroke="var(--blue)" stroke-width=".8"/>
    <polyline points="134,28 148,18 162,24 176,14 190,26 204,14 218,26" fill="none" stroke="var(--green)" stroke-width=".8"/>
    <g font-family="Arimo,Arial,sans-serif" font-size="2.2" fill="#555"><path d="M88 46h4" stroke="var(--green)"/><text x="93" y="47">Text</text><path d="M88 50h4" stroke="var(--blue)"/><text x="93" y="51">Text</text><path d="M208 46h4" stroke="var(--green)"/><text x="213" y="47">Text</text><path d="M208 50h4" stroke="var(--blue)"/><text x="213" y="51">Text</text></g>
  </svg>
  <div class="txt" style="left:18px;top:111px;width:100px">Lorem ipsum dolor sit amet, consetetur sadipscing elitr, sed diam nonumy eirmod tempor invidunt ut labore et dolore magna aliquyam erat, sed diam</div>
  <div class="txt" style="left:138px;top:111px;width:100px">Lorem ipsum dolor sit amet, consetetur sadipscing elitr, sed diam nonumy eirmod tempor invidunt ut labore et dolore magna aliquyam erat, sed diam</div>
  <div class="bar-bottom"></div>
</section>

<section class="slide" style="left:328px;top:582px">
  <div class="bar-top"></div>
  <div class="title">LOREM IPSUM DOLOR SIT AMET</div>
  <div class="logo"><i></i>VELSORI</div>
  <svg width="240" height="112" viewBox="0 0 240 112" style="left:12px;top:26px">
    <g font-family="Arimo,Arial,sans-serif" font-size="3.2" fill="#222"><text x="2" y="4">Title <tspan font-size="1.8">(Text)</tspan></text><text x="122" y="4">Title <tspan font-size="1.8">(Text)</tspan></text><text x="2" y="58">Title <tspan font-size="1.8">(Text)</tspan></text><text x="122" y="58">Title <tspan font-size="1.8">(Text)</tspan></text></g>
    <g stroke="#e6e6e6" stroke-width=".3"><path d="M6 10H112M6 16H112M6 22H112M6 28H112M6 34H112M6 40H112M126 10H232M126 16H232M126 22H232M126 28H232M126 34H232M126 40H232M6 64H112M6 72H112M6 80H112M6 88H112M6 96H112M126 64H232M126 72H232M126 80H232M126 88H232M126 96H232"/></g>
    <polyline points="8,34 16,30 24,16 32,14 40,20 48,21 56,22 64,20 72,22 80,24 88,22 96,20 104,20" fill="none" stroke="var(--blue)" stroke-width=".7"/>
    <polyline points="8,36 16,32 24,18 32,20 40,22 48,23 56,26 64,24 72,28 80,26 88,22 96,24 104,22" fill="none" stroke="var(--green)" stroke-width=".7"/>
    <polyline points="128,36 136,18 144,24 152,26 160,22 168,26 176,24 184,26 192,24 200,28 208,24 216,26 224,24" fill="none" stroke="var(--blue)" stroke-width=".7"/>
    <polyline points="128,34 136,20 144,28 152,30 160,26 168,30 176,26 184,28 192,30 200,30 208,26 216,28" fill="none" stroke="var(--green)" stroke-width=".7"/>
    <g fill="var(--blue)"><rect x="10" y="80" width="1.6" height="16"/><rect x="17" y="76" width="1.6" height="20"/><rect x="24" y="74" width="1.6" height="22"/><rect x="31" y="78" width="1.6" height="18"/><rect x="38" y="82" width="1.6" height="14"/><rect x="45" y="80" width="1.6" height="16"/><rect x="52" y="78" width="1.6" height="18"/><rect x="59" y="80" width="1.6" height="16"/><rect x="66" y="76" width="1.6" height="20"/><rect x="73" y="82" width="1.6" height="14"/><rect x="80" y="78" width="1.6" height="18"/><rect x="87" y="76" width="1.6" height="20"/><rect x="94" y="80" width="1.6" height="16"/><rect x="101" y="78" width="1.6" height="18"/>
    <rect x="130" y="84" width="1.6" height="12"/><rect x="137" y="76" width="1.6" height="20"/><rect x="144" y="86" width="1.6" height="10"/><rect x="151" y="70" width="1.6" height="26"/><rect x="158" y="72" width="1.6" height="24"/><rect x="165" y="78" width="1.6" height="18"/><rect x="172" y="72" width="1.6" height="24"/><rect x="179" y="76" width="1.6" height="20"/><rect x="186" y="70" width="1.6" height="26"/><rect x="193" y="78" width="1.6" height="18"/><rect x="200" y="72" width="1.6" height="24"/><rect x="207" y="76" width="1.6" height="20"/></g>
    <g fill="var(--green)"><rect x="12" y="82" width="1.6" height="14"/><rect x="19" y="78" width="1.6" height="18"/><rect x="26" y="78" width="1.6" height="18"/><rect x="33" y="80" width="1.6" height="16"/><rect x="40" y="80" width="1.6" height="16"/><rect x="47" y="84" width="1.6" height="12"/><rect x="54" y="80" width="1.6" height="16"/><rect x="61" y="82" width="1.6" height="14"/><rect x="68" y="80" width="1.6" height="16"/><rect x="75" y="80" width="1.6" height="16"/><rect x="82" y="82" width="1.6" height="14"/><rect x="89" y="80" width="1.6" height="16"/><rect x="96" y="82" width="1.6" height="14"/><rect x="103" y="80" width="1.6" height="16"/>
    <rect x="132" y="86" width="1.6" height="10"/><rect x="139" y="80" width="1.6" height="16"/><rect x="146" y="82" width="1.6" height="14"/><rect x="153" y="80" width="1.6" height="16"/><rect x="160" y="82" width="1.6" height="14"/><rect x="167" y="80" width="1.6" height="16"/><rect x="174" y="84" width="1.6" height="12"/><rect x="181" y="80" width="1.6" height="16"/><rect x="188" y="82" width="1.6" height="14"/><rect x="195" y="80" width="1.6" height="16"/><rect x="202" y="84" width="1.6" height="12"/><rect x="209" y="80" width="1.6" height="16"/></g>
    <g font-family="Arimo,Arial,sans-serif" font-size="1.8" fill="#555"><text x="8" y="46">Text Text Text Text Text Text Text Text Text Text Text Text</text><text x="128" y="46">Text Text Text Text Text Text Text Text Text Text Text Text</text><text x="8" y="100">Text Text Text Text Text Text Text Text Text Text Text Text</text><text x="128" y="100">Text Text Text Text Text Text Text Text Text Text Text Text</text>
    <rect x="108" y="22" width="2" height="1" fill="var(--blue)"/><rect x="228" y="22" width="2" height="1" fill="var(--blue)"/><rect x="108" y="25" width="2" height="1" fill="var(--green)"/><rect x="228" y="25" width="2" height="1" fill="var(--green)"/></g>
  </svg>
  <div class="bar-bottom"></div>
</section>

<section class="slide" style="left:612px;top:582px">
  <div class="bar-top"></div>
  <div class="title">LOREM IPSUM DOLOR SIT AMET</div>
  <div class="logo"><i></i>VELSORI</div>
  <svg width="240" height="100" viewBox="0 0 240 100" style="left:14px;top:34px">
    <g font-family="Arimo,Arial,sans-serif" font-size="2.4" fill="#555">
      <text x="2" y="3" font-size="3.8" fill="#222">Title <tspan font-size="2">(Text)</tspan></text>
      <text x="160" y="3" font-size="3.8" fill="#222">Title <tspan font-size="2">(Text)</tspan></text>
      <text x="2" y="12">Text</text><text x="2" y="19.5">Text</text><text x="2" y="27">Text</text><text x="2" y="34.5">Text</text><text x="2" y="42">Text</text><text x="2" y="49.5">Text</text><text x="2" y="57">Text</text><text x="2" y="64.5">Text</text><text x="2" y="72">Text</text><text x="2" y="79.5">Text</text>
    </g>
    <g fill="var(--green)">
      <rect x="12" y="9" width="110" height="3.6"/><rect x="12" y="16.5" width="92" height="3.6"/><rect x="12" y="24" width="92" height="3.6"/><rect x="12" y="31.5" width="80" height="3.6"/><rect x="12" y="39" width="74" height="3.6"/><rect x="12" y="46.5" width="66" height="3.6"/><rect x="12" y="54" width="62" height="3.6"/><rect x="12" y="61.5" width="44" height="3.6"/><rect x="12" y="69" width="40" height="3.6"/><rect x="12" y="76.5" width="36" height="3.6"/>
      <rect x="180" y="9" width="16" height="3.6"/><rect x="180" y="16.5" width="22" height="3.6"/><rect x="172" y="24" width="8" height="3.6"/><rect x="176" y="31.5" width="4" height="3.6"/><rect x="180" y="39" width="16" height="3.6"/><rect x="180" y="46.5" width="16" height="3.6"/><rect x="180" y="54" width="6" height="3.6"/><rect x="176" y="61.5" width="4" height="3.6"/><rect x="180" y="69" width="22" height="3.6"/><rect x="180" y="76.5" width="8" height="3.6"/>
    </g>
    <g font-family="Arimo,Arial,sans-serif" font-size="2.2" fill="#444">
      <text x="124" y="12">31</text><text x="106" y="19.5">29</text><text x="106" y="27">29</text><text x="94" y="34.5">26</text><text x="88" y="42">24</text><text x="80" y="49.5">22</text><text x="76" y="57">21</text><text x="58" y="64.5">17</text><text x="54" y="72">14</text><text x="50" y="79.5">13</text>
      <text x="198" y="12">+3%</text><text x="204" y="19.5">+4%</text><text x="164" y="27">-2%</text><text x="168" y="34.5">-1%</text><text x="198" y="42">+3%</text><text x="198" y="49.5">+3%</text><text x="188" y="57">+1%</text><text x="168" y="64.5">-1%</text><text x="204" y="72">+4%</text><text x="190" y="79.5">+2%</text>
    </g>
  </svg>
  <div class="bar-bottom"></div>
</section>

<section class="slide" style="left:896px;top:582px">
  <div class="bar-top"></div>
  <div class="title">LOREM IPSUM DOLOR SIT AMET</div>
  <div class="sub">Consetetur sadipscing elitr</div>
  <div class="logo"><i></i>VELSORI</div>
  <table class="tbl" style="left:16px;top:44px;width:222px;font-size:2.3px">
    <tr><th style="background:none;width:54px"></th><th style="text-align:left">Text</th><th style="text-align:left;border-left:2px solid #fff">Text</th><th style="text-align:left;border-left:2px solid #fff">Text</th></tr>
    <tr><td style="height:18px">Text</td><td style="text-align:left;line-height:3px">Lorem ipsum dolor sit amet, consetetur sadipscing elitr, sed diam nonumy eirmod tempor invidunt ut labore et dolore</td><td style="text-align:left;line-height:3px">Lorem ipsum dolor sit amet, consetetur sadipscing elitr, sed diam nonumy eirmod tempor invidunt ut labore et dolore</td><td style="text-align:left;line-height:3px">Lorem ipsum dolor sit amet, consetetur sadipscing elitr, sed diam nonumy eirmod tempor invidunt ut labore et dolore</td></tr>
    <tr><td style="height:18px">Text</td><td style="text-align:left;line-height:3px">Lorem ipsum dolor sit amet, consetetur sadipscing elitr, sed diam nonumy eirmod tempor invidunt ut labore et dolore</td><td style="text-align:left;line-height:3px">Lorem ipsum dolor sit amet, consetetur sadipscing elitr, sed diam nonumy eirmod tempor invidunt ut labore et dolore</td><td style="text-align:left;line-height:3px">Lorem ipsum dolor sit amet, consetetur sadipscing elitr, sed diam nonumy eirmod tempor invidunt ut labore et dolore</td></tr>
    <tr><td style="height:18px">Text</td><td style="text-align:left;line-height:3px">Lorem ipsum dolor sit amet, consetetur sadipscing elitr, sed diam nonumy eirmod tempor invidunt ut labore et dolore</td><td style="text-align:left;line-height:3px">Lorem ipsum dolor sit amet, consetetur sadipscing elitr, sed diam nonumy eirmod tempor invidunt ut labore et dolore</td><td style="text-align:left;line-height:3px">Lorem ipsum dolor sit amet, consetetur sadipscing elitr, sed diam nonumy eirmod tempor invidunt ut labore et dolore</td></tr>
    <tr><td style="height:18px">Text</td><td style="text-align:left;line-height:3px">Lorem ipsum dolor sit amet, consetetur sadipscing elitr, sed diam nonumy eirmod tempor invidunt ut labore et dolore</td><td style="text-align:left;line-height:3px">Lorem ipsum dolor sit amet, consetetur sadipscing elitr, sed diam nonumy eirmod tempor invidunt ut labore et dolore</td><td style="text-align:left;line-height:3px">Lorem ipsum dolor sit amet, consetetur sadipscing elitr, sed diam nonumy eirmod tempor invidunt ut labore et dolore</td></tr>
  </table>
  <div class="bar-bottom"></div>
</section>

<!-- Row 5 -->
<section class="slide" style="left:43px;top:764px">
  <div class="bar-top"></div>
  <div class="title">LOREM IPSUM DOLOR SIT AMET</div>
  <div class="sub">Consetetur sadipscing elitr</div>
  <div class="logo"><i></i>VELSORI</div>
  <table class="tbl" style="left:16px;top:46px;width:222px">
    <tr><td style="border:0"></td><td style="border:0;text-align:left">Text</td><td style="border:0;text-align:left">Text</td><td style="border:0;text-align:left">Text</td></tr>
    <tr><td colspan="4" style="background:var(--green);color:#fff;height:5px">Title</td></tr>
    <tr><td style="width:60px"></td><td style="text-align:left">Text</td><td style="text-align:left">Text</td><td style="text-align:left">Text</td></tr>
    <tr><td></td><td style="text-align:left">Text</td><td style="text-align:left">Text</td><td style="text-align:left">Text</td></tr>
    <tr><td></td><td style="text-align:left">Text</td><td style="text-align:left">Text</td><td style="text-align:left">Text</td></tr>
    <tr><td colspan="4" style="background:var(--green);color:#fff;height:5px">Title</td></tr>
    <tr><td></td><td style="text-align:left">Text</td><td style="text-align:left">Text</td><td style="text-align:left">Text</td></tr>
    <tr><td></td><td style="text-align:left">Text</td><td style="text-align:left">Text</td><td style="text-align:left">Text</td></tr>
    <tr><td></td><td style="text-align:left">Text</td><td style="text-align:left">Text</td><td style="text-align:left">Text</td></tr>
  </table>
  <div class="bar-bottom"></div>
</section>

<section class="slide" style="left:328px;top:764px">
  <div class="bar-top"></div>
  <div class="title">LOREM IPSUM DOLOR SIT AMET</div>
  <div class="sub">Consetetur sadipscing elitr</div>
  <div class="logo"><i></i>VELSORI</div>
  <table class="tbl" style="left:16px;top:43px;width:112px">
    <tr><th>Text</th><th>Text</th><th>Text</th><th>Text</th><th>Text</th></tr>
    <tr><td style="height:11px">Text</td><td>11</td><td>12</td><td>17</td><td>18</td></tr>
    <tr><td style="height:11px">Text</td><td>56</td><td>60</td><td>80</td><td>84</td></tr>
    <tr><td style="height:11px">Text</td><td>21</td><td>22</td><td>27</td><td>28</td></tr>
    <tr><td style="height:11px">Text</td><td>14</td><td>14</td><td>17</td><td>19</td></tr>
    <tr><td style="height:11px">Text</td><td>4</td><td>4</td><td>5</td><td>5</td></tr>
    <tr class="total"><td>Text</td><td>106</td><td>112</td><td>146</td><td>154</td></tr>
  </table>
  <div style="position:absolute;left:145px;top:43px;width:90px;height:7px;background:var(--green);color:#fff;font-size:3px;text-align:center;line-height:7px">Title</div>
  <ul class="txt bullets" style="left:148px;top:54px;width:86px">
    <li>Lorem ipsum dolor sit amet, consetetur sadipscing elitr, sed diam nonumy eirmod tempor invidunt ut labore et dolore magna</li>
    <li>Lorem ipsum dolor sit amet, consetetur sadipscing elitr, sed diam nonumy eirmod tempor invidunt ut labore et dolore magna</li>
    <li>Lorem ipsum dolor sit amet, consetetur sadipscing elitr, sed diam nonumy eirmod tempor invidunt ut labore et dolore magna</li>
    <li>Lorem ipsum dolor sit amet, consetetur sadipscing elitr, sed diam nonumy eirmod tempor invidunt ut labore et dolore magna</li>
  </ul>
  <div class="bar-bottom"></div>
</section>

<section class="slide" style="left:612px;top:764px">
  <div class="bar-top"></div>
  <div class="title">LOREM IPSUM DOLOR SIT AMET</div>
  <div class="sub">Consetetur sadipscing elitr</div>
  <div class="logo"><i></i>VELSORI</div>
  <table class="tbl" style="left:16px;top:40px;width:96px;font-size:2.2px;border:.4px solid var(--green)">
    <tr><th>Text</th><th>Text</th><th>Text</th><th>Δ</th></tr>
    <tr><td style="height:4.6px">Text</td><td>12</td><td>14</td><td>+2</td></tr>
    <tr><td style="height:4.6px">Text</td><td>11</td><td>9</td><td>-2</td></tr>
    <tr><td style="height:4.6px">Text</td><td>14</td><td>6</td><td>-8</td></tr>
    <tr><td style="height:4.6px">Text</td><td>9</td><td>12</td><td>+3</td></tr>
    <tr><td style="height:4.6px">Text</td><td>11</td><td>12</td><td>+1</td></tr>
    <tr class="total"><td>Total</td><td>57</td><td>53</td><td>-4</td></tr>
    <tr><td style="height:4.6px">Text</td><td>9</td><td>12</td><td>+3</td></tr>
    <tr><td style="height:4.6px">Text</td><td>6</td><td>11</td><td>+5</td></tr>
    <tr><td style="height:4.6px">Text</td><td>9</td><td>10</td><td>+1</td></tr>
    <tr><td style="height:4.6px">Text</td><td>7</td><td>9</td><td>+2</td></tr>
    <tr><td style="height:4.6px">Text</td><td>11</td><td>11</td><td>+0</td></tr>
    <tr class="total"><td>Total</td><td>42</td><td>53</td><td>+11</td></tr>
  </table>
  <table class="tbl" style="left:114px;top:40px;width:56px;font-size:2.2px;border:.4px solid var(--green)">
    <tr><th>Text</th><th>Text</th><th>Δ</th></tr>
    <tr><td style="height:4.6px">59</td><td>55</td><td>-4</td></tr>
    <tr><td style="height:4.6px">56</td><td>59</td><td>+3</td></tr>
    <tr><td style="height:4.6px">53</td><td>61</td><td>+8</td></tr>
    <tr><td style="height:4.6px">45</td><td>40</td><td>-5</td></tr>
    <tr><td style="height:4.6px">44</td><td>42</td><td>-2</td></tr>
    <tr class="total"><td>257</td><td>257</td><td>+0</td></tr>
    <tr><td style="height:4.6px">35</td><td>36</td><td>+1</td></tr>
    <tr><td style="height:4.6px">32</td><td>34</td><td>+2</td></tr>
    <tr><td style="height:4.6px">41</td><td>38</td><td>-3</td></tr>
    <tr><td style="height:4.6px">34</td><td>31</td><td>-3</td></tr>
    <tr><td style="height:4.6px">29</td><td>31</td><td>+2</td></tr>
    <tr class="total"><td>171</td><td>170</td><td>-1</td></tr>
  </table>
  <ul class="txt bullets" style="left:180px;top:62px;width:58px">
    <li>Lorem ipsum dolor sit amet, consetetur sadipscing elitr, sed diam nonumy eirmod tempor invidunt ut labore et dolore</li>
    <li>Lorem ipsum dolor sit amet, consetetur sadipscing elitr, sed diam nonumy eirmod tempor invidunt ut labore et dolore</li>
  </ul>
  <div class="bar-bottom"></div>
</section>

<section class="slide" style="left:896px;top:764px">
  <div class="bar-top"></div>
  <div class="title">LOREM IPSUM DOLOR SIT AMET</div>
  <div class="sub">Consetetur sadipscing elitr</div>
  <div class="logo"><i></i>VELSORI</div>
  <ul class="txt bullets" style="left:18px;top:46px;width:52px">
    <li>Lorem ipsum dolor sit amet, consetetur sadipscing elitr, sed diam nonumy eirmod tempor invidunt ut labore et dolore</li>
    <li>Lorem ipsum dolor sit amet, consetetur sadipscing elitr, sed diam nonumy eirmod tempor invidunt ut labore et dolore</li>
  </ul>
  <svg width="150" height="50" viewBox="0 0 150 50" style="left:85px;top:36px">
    <g fill="var(--green)"><rect x="8" y="37" width="8" height="11"/><rect x="30" y="31" width="8" height="17"/><rect x="52" y="17" width="8" height="31"/><rect x="74" y="8" width="8" height="40"/><rect x="96" y="23" width="8" height="25"/><rect x="118" y="28" width="8" height="20"/></g>
    <g font-family="Arimo,Arial,sans-serif" font-size="2.6" fill="#444" text-anchor="middle"><text x="12" y="35">17</text><text x="34" y="29">28</text><text x="56" y="15">53</text><text x="78" y="6">66</text><text x="100" y="21">45</text><text x="122" y="26">34</text></g>
    <line x1="2" y1="48" x2="132" y2="48" stroke="#999" stroke-width=".3"/>
  </svg>
  <table class="tbl" style="left:18px;top:89px;width:220px;font-size:2.2px;border:.4px solid var(--green)">
    <tr><th>Text</th><th>Text</th><th>Text</th><th>Text</th><th>Text</th><th>Text</th><th>Text</th></tr>
    <tr><td style="height:4.6px">Text</td><td>30</td><td>21</td><td>12</td><td>13</td><td>24</td><td>15</td></tr>
    <tr><td style="height:4.6px">Text</td><td>54</td><td>56</td><td>60</td><td>46</td><td>68</td><td>72</td></tr>
    <tr><td style="height:4.6px">Text</td><td>20</td><td>21</td><td>22</td><td>23</td><td>24</td><td>25</td></tr>
    <tr><td style="height:4.6px">Text</td><td>13</td><td>14</td><td>16</td><td>17</td><td>18</td><td>19</td></tr>
    <tr><td style="height:4.6px">Text</td><td>31</td><td>32</td><td>34</td><td>36</td><td>38</td><td>40</td></tr>
  </table>
  <div class="bar-bottom"></div>
</section>

</div>
</body>
</html>
```